KeyBridge needs a modern business card

We are a modern conveyancing company and we need to appeal to the top (Multi-million dollar properties)and bottom on the property conveyancing market but our sweet spot is the middle of the market. I like professional with a hint of unconventional.

Target Market(s)

As above

Industry/Entity Type

Real Estate

Contact Information for Business Card

Back Of card:
thinking black with the logo and a tag line (I could be wrong about the black)
Tag line - Sound Advice, Seamless Settlements

Front of Card:
Marissa Doyle (BBus (Finance) LLB)
Licensed Conveyancer
Email: marissa@keybridge.com.au

Key Bridge
ABN: 41 836 907
Suite 14, Level 3, 9 Harlow Avenue Westmead, NSW 2145
Phone: 1300 782 916

Sydney - Melbourne - Brisbane (Perhaps have this along the bottom of the card)

Requirements
Must have
• Sleek, modern and top end appeal (But approachable)
Should not have
• Not too cluttered

```html
<!DOCTYPE html>
<html lang="en">
<head>
<meta charset="utf-8">
<title>KeyBridge – Business Card</title>
<link rel="stylesheet" href="https://fonts.googleapis.com/css2?family=Questrial&display=swap">
<style>
  :root {
    --page: #e6e6e4;
    --card: #1f1d1e;
    --band: #0b4a72;
    --band-line: #0e5a88;
    --white: #ffffff;
    --soft-white: #e9eef2;
    --band-text: #d7ecfa;
    --accent-cyan: #5cc9f2;
    --font: "Questrial", "Century Gothic", sans-serif;
  }
  * { box-sizing: border-box; margin: 0; padding: 0; }
  html, body {
    width: 1200px; height: 900px; overflow: hidden;
    background: var(--page);
    font-family: var(--font);
  }
  .canvas {
    position: relative; width: 1200px; height: 900px;
    display: flex; flex-direction: column; align-items: center; justify-content: center;
    gap: 40px;
  }
  .card {
    position: relative; width: 640px; height: 391px;
    background: var(--card);
    box-shadow: 0 6px 18px rgba(0,0,0,.25);
    overflow: hidden;
    color: var(--white);
  }
  /* Back of card */
  .brand {
    position: absolute; left: 0; right: 0; top: 110px;
    display: flex; align-items: center; justify-content: center; gap: 14px;
  }
  .brand-square { width: 30px; height: 30px; background: var(--accent-cyan); }
  .brand-name { font-size: 42px; font-weight: 400; color: var(--white); letter-spacing: .5px; }
  .tagline-band {
    position: absolute; left: 0; right: 0; top: 230px; height: 44px;
    background: var(--band);
    display: flex; align-items: center; justify-content: center;
  }
  .tagline {
    font-size: 21px; text-transform: uppercase; letter-spacing: .6px;
    color: var(--soft-white);
  }
  /* Front of card */
  .contact {
    position: absolute; left: 44px; top: 24px;
    font-style: italic; color: var(--soft-white);
  }
  .person-name {
    font-style: normal; font-weight: 400; font-size: 26px; text-transform: uppercase;
    color: var(--white); margin-bottom: 4px; letter-spacing: .3px; line-height: 1.2;
  }
  .credentials, .role { font-size: 16px; line-height: 1.45; }
  .email {
    display: flex; align-items: center; gap: 8px;
    font-size: 17px; margin-top: 10px;
  }
  .company { margin-top: 22px; font-size: 17px; line-height: 1.4; }
  .phone { display: flex; align-items: center; gap: 4px; }
  .icon { display: block; flex: none; }
  .cities-band {
    position: absolute; left: 0; right: 0; bottom: 26px; height: 54px;
    background: var(--band);
    border-top: 1px solid var(--band-line);
    display: flex; align-items: center; padding-left: 36px;
  }
  .cities { font-size: 27px; color: var(--band-text); }
  .front-brand {
    position: absolute; right: 44px; top: 150px;
    display: flex; align-items: center; gap: 12px;
  }
  .front-brand .brand-square { width: 22px; height: 22px; }
  .front-brand .brand-name { font-size: 30px; }
</style>
</head>
<body>
<main class="canvas">

  <section class="card card-back" aria-label="Back of business card">
    <div class="brand">
      <span class="brand-square" aria-hidden="true"></span>
      <span class="brand-name">KeyBridge</span>
    </div>
    <div class="tagline-band">
      <p class="tagline">Sound Advice, Seamless Settlements</p>
    </div>
  </section>

  <section class="card card-front" aria-label="Front of business card">
    <div class="contact">
      <h1 class="person-name">Marissa Doyle</h1>
      <p class="credentials">(BBus (Finance) LLB)</p>
      <p class="role">Licensed Conveyancer</p>
      <p class="email">
        <svg class="icon" width="22" height="15" viewBox="0 0 22 15" aria-hidden="true">
          <rect x="1" y="1" width="20" height="13" fill="none" stroke="#e9eef2" stroke-width="1.3"/>
          <path d="M1 1 L11 9 L21 1 M1 14 L8 7 M21 14 L14 7" fill="none" stroke="#e9eef2" stroke-width="1.3"/>
        </svg>
        marissa@keybridge.com.au
      </p>
      <div class="company">
        <p>Key Bridge</p>
        <p>ABN: 41 836 907</p>
        <p>Suite 14, Level 3, 9 Harlow Avenue</p>
        <p>Westmead, NSW 2145</p>
        <p class="phone">
          <svg class="icon" width="20" height="20" viewBox="0 0 22 22" aria-hidden="true">
            <circle cx="11" cy="11" r="10" fill="none" stroke="#e9eef2" stroke-width="1.4"/>
            <path d="M8 5.5 C6.5 6.5 6 8.5 7.5 11.5 C9 14.5 11 16.3 13.5 16.5 L14.8 15 L12.8 13 L11.6 13.8 C10.5 13 9.5 11.5 9.1 10.2 L10.2 9.2 L9.3 6.5 Z" fill="#e9eef2"/>
          </svg>
          1300 782 916
        </p>
      </div>
    </div>
    <div class="front-brand">
      <span class="brand-square" aria-hidden="true"></span>
      <span class="brand-name">KeyBridge</span>
    </div>
    <div class="cities-band">
      <p class="cities">Sydney - Melbourne - Brisbane</p>
    </div>
  </section>

</main>
</body>
</html>
```